New Business Card Design Project

We are a spa looking to create a professional elegant business card for a spa mainly black and white with a splash of lime green. This card will be two sided - the front side will have an image, the logo, and the spa's information - the back side will have a promotion for new customers - NEW CUSTOMERS $20 OFF

Look and feel: chic, modern, and spa-ish.
Information to be included:
Therapist Name
Therapist specialty
Address: 5174 Marlowe Ave, Beverly Hills CA 90211
Phone: (310) 482-3957

Let me know if you have any questions!

Thank you

Industry/Entity Type

Business

```html
<!DOCTYPE html>
<html lang="en">
<head>
<meta charset="utf-8">
<title>Vela Day Spa – Business Card</title>
<link rel="stylesheet" href="https://fonts.googleapis.com/css2?family=Tinos:wght@400&family=PT+Sans:ital,wght@0,400;1,400&display=swap">
<style>
  :root {
    --backdrop: #2b2b2b;
    --card-light: #f1f2f2;
    --card-shade: #dfe0e1;
    --ink: #111111;
    --text: #2a2a2a;
    --lime: #8dc63f;
  }
  * { margin: 0; padding: 0; box-sizing: border-box; }
  html, body {
    width: 1200px;
    height: 800px;
    overflow: hidden;
    background: var(--backdrop);
  }
  .canvas {
    width: 1200px;
    height: 800px;
    display: flex;
    flex-direction: column;
    align-items: center;
    justify-content: center;
    gap: 36px;
  }
  .business-card {
    position: relative;
    width: 600px;
    height: 343px;
    overflow: hidden;
    box-shadow: 0 10px 30px rgba(0,0,0,0.45);
  }
  .card-texture {
    position: absolute;
    inset: 0;
    background: radial-gradient(ellipse at 50% 45%, var(--card-light) 0%, var(--card-shade) 100%);
  }
  .brand {
    display: flex;
    align-items: center;
    gap: 12px;
  }
  .brand-circle {
    width: 30px;
    height: 30px;
    border: 3px solid var(--ink);
    border-radius: 50%;
    flex: none;
  }
  .brand-name {
    font-family: "Tinos", serif;
    font-weight: 400;
    font-size: 34px;
    color: var(--ink);
    letter-spacing: 1px;
    white-space: nowrap;
  }

  /* Front side */
  .card-front .card-content {
    position: relative;
    height: 100%;
    display: flex;
    flex-direction: column;
    align-items: center;
    padding-top: 46px;
  }
  .therapist-name {
    margin-top: 34px;
    font-family: "Tinos", serif;
    font-weight: 400;
    font-size: 34px;
    color: var(--ink);
    line-height: 1;
  }
  .therapist-role {
    margin-top: 4px;
    font-family: "PT Sans", sans-serif;
    font-style: italic;
    font-size: 21px;
    color: var(--lime);
  }
  .contact-list {
    list-style: none;
    margin-top: 30px;
    display: flex;
    flex-direction: column;
    align-items: center;
    gap: 10px;
    font-family: "PT Sans", sans-serif;
    font-size: 17px;
    color: var(--text);
  }
  .contact-item {
    display: flex;
    align-items: center;
    gap: 6px;
  }
  .contact-icon { width: 19px; height: 19px; fill: var(--lime); }
  .contact-icon.phone { fill: none; stroke: var(--lime); stroke-width: 2; }

  /* Back side */
  .card-back .card-content {
    position: relative;
    height: 100%;
    display: flex;
    flex-direction: column;
    align-items: center;
    justify-content: center;
    gap: 30px;
  }
  .promo {
    font-family: "Tinos", serif;
    font-weight: 400;
    font-size: 30px;
    letter-spacing: 1px;
    text-transform: uppercase;
    color: var(--lime);
    white-space: nowrap;
  }
</style>
</head>
<body>
<main class="canvas">
  <article class="business-card card-front">
    <div class="card-texture" role="img" aria-label="Soft light grey damask pattern covering the card background"></div>
    <div class="card-content">
      <div class="brand">
        <span class="brand-circle"></span>
        <span class="brand-name">Vela Day Spa</span>
      </div>
      <h1 class="therapist-name">Evan Hale</h1>
      <p class="therapist-role">therapist</p>
      <ul class="contact-list">
        <li class="contact-item">
          <svg class="contact-icon" viewBox="0 0 24 24" aria-hidden="true"><path d="M12 3 2 12h3v9h5v-6h4v6h5v-9h3z"/></svg>
          <span>5174 Marlowe Ave, Beverly Hills CA 90211</span>
        </li>
        <li class="contact-item">
          <svg class="contact-icon phone" viewBox="0 0 24 24" aria-hidden="true"><path d="M5 3h4l2 5-2.5 1.5a11 11 0 0 0 6 6L16 13l5 2v4a2 2 0 0 1-2 2A16 16 0 0 1 3 5a2 2 0 0 1 2-2z"/></svg>
          <span>(310) 482-3957</span>
        </li>
      </ul>
    </div>
  </article>

  <article class="business-card card-back">
    <div class="card-texture" role="img" aria-label="Soft light grey damask pattern covering the card background"></div>
    <div class="card-content">
      <div class="brand">
        <span class="brand-circle"></span>
        <span class="brand-name">Vela Day Spa</span>
      </div>
      <p class="promo">New Customers $20 Off</p>
    </div>
  </article>
</main>
</body>
</html>
```